Custom Office Whiteboard for Staff

I need a custom whiteboard layout design. All fields are contained in the attached images along with artwork requirements including required bleed. Size will be 1200mm x 900mm.

Feel free to make is more visually appealing than this draft.

Use colors blue, black and white to keep company feel.

Font styles to use
Sans Serif

Colors
ffffff
000000
33a6d7

```html
<!DOCTYPE html>
<html lang="en">
<head>
<meta charset="utf-8">
<title>Skyward Ballooning – Staff Whiteboard</title>
<link href="https://fonts.googleapis.com/css2?family=Roboto+Condensed:wght@400;700&family=Roboto:wght@400;900&display=swap" rel="stylesheet">
<style>
  :root{
    --navy:#0b2540;
    --blue:#1e96d1;
    --row-tint:#dde9f5;
    --grid:#b8c6d4;
    --white:#ffffff;
    --ink:#000000;
    --notes:#fdf0eb;
  }
  *{box-sizing:border-box;margin:0;padding:0}
  html,body{width:1200px;height:900px;overflow:hidden;background:var(--white)}
  .board{position:relative;width:1200px;height:900px;overflow:hidden;background:var(--white);font-family:"Roboto",Arial,sans-serif;color:var(--ink)}
  .backdrop{position:absolute;inset:0}
  .brand{position:absolute;left:48px;top:48px;display:flex;align-items:center;gap:12px;font-family:"Roboto Condensed",Arial,sans-serif;font-weight:700;font-size:34px;color:var(--navy)}
  .brand-dot{width:22px;height:22px;border-radius:50%;background:var(--blue)}
  .contact{position:absolute;right:30px;top:26px;text-align:right;font-family:"Roboto Condensed",Arial,sans-serif;font-size:24px;line-height:30px;color:var(--ink)}
  .panel{position:absolute}
  table{width:100%;border-collapse:collapse;table-layout:fixed}
  .panel-title{background:var(--navy);color:var(--white);font-family:"Roboto Condensed",Arial,sans-serif;font-weight:700;text-align:center}
  th{background:var(--navy);color:var(--white);font-family:"Roboto Condensed",Arial,sans-serif;font-weight:400;font-size:13px;line-height:12px;border:1px solid #3a5670}
  td{border:1px solid var(--grid);background:var(--white);font-size:10.5px;text-align:center;white-space:nowrap;overflow:hidden}
  tr:nth-child(odd) td{background:var(--row-tint)}
  .crew{left:41px;top:153px;width:704px}
  .crew .panel-title{height:29px;line-height:29px;font-size:18px}
  .crew th{height:30px}
  .crew td{height:29.5px}
  .notes{position:absolute;left:770px;top:150px;width:314px;height:415px;background:var(--notes);box-shadow:0 0 3px rgba(0,0,0,.15);text-align:center}
  .notes h2{font-family:"Roboto",Arial,sans-serif;font-weight:900;font-size:56px;margin-top:20px;letter-spacing:1px}
  .tasks-6{left:41px;top:584px;width:269px}
  .tasks-12{left:334px;top:584px;width:269px}
  .schedule{left:630px;top:582px;width:538px}
  .small .panel-title{height:24px;line-height:24px;font-size:17px}
  .small th{height:25px}
  .small td{height:24.4px}
  .footer{position:absolute;left:0;right:0;top:843px;text-align:center;font-family:"Roboto Condensed",Arial,sans-serif;font-size:23px;color:var(--white);word-spacing:2px}
  .footer span{margin:0 14px}
</style>
</head>
<body>
<div class="board">
  <svg class="backdrop" width="1200" height="900" viewBox="0 0 1200 900" aria-hidden="true">
    <path d="M0,230 C260,120 620,70 1200,190 L1200,270 C1000,215 760,160 450,150 C250,150 100,200 0,230 Z" fill="#1e96d1"/>
    <path d="M0,800 C220,760 500,745 760,752 C960,760 1110,830 1200,900 L0,900 Z" fill="#1e96d1"/>
  </svg>

  <div class="brand"><span class="brand-dot"></span>Skyward Ballooning</div>

  <div class="contact">
    <div>Email: hello@skywardballooning.com.au</div>
    <div>Web: www.skywardballooning.com.au</div>
    <div>Phone: 1300 555 019</div>
  </div>

  <section class="panel crew">
    <div class="panel-title">Flight / Ground Crew</div>
    <table>
      <thead><tr><th>Crew Name</th><th>License Class</th><th>Medical</th><th>BFR</th><th>Instructor Rating</th><th>CAO 20.11</th><th>DAMP</th><th>Maintenance Authority</th><th>ASIC</th></tr></thead>
      <tbody>
        <tr><td></td><td></td><td></td><td></td><td></td><td></td><td></td><td></td><td></td></tr>
        <tr><td></td><td></td><td></td><td></td><td></td><td></td><td></td><td></td><td></td></tr>
        <tr><td></td><td></td><td></td><td></td><td></td><td></td><td></td><td></td><td></td></tr>
        <tr><td></td><td></td><td></td><td></td><td></td><td></td><td></td><td></td><td></td></tr>
        <tr><td></td><td></td><td></td><td></td><td></td><td></td><td></td><td></td><td></td></tr>
        <tr><td></td><td></td><td></td><td></td><td></td><td></td><td></td><td></td><td></td></tr>
        <tr><td></td><td></td><td></td><td></td><td></td><td></td><td></td><td></td><td></td></tr>
        <tr><td></td><td></td><td></td><td></td><td></td><td></td><td></td><td></td><td></td></tr>
        <tr><td></td><td></td><td></td><td></td><td></td><td></td><td></td><td></td><td></td></tr>
        <tr><td></td><td></td><td></td><td></td><td></td><td></td><td></td><td></td><td></td></tr>
        <tr><td></td><td></td><td></td><td></td><td></td><td></td><td></td><td></td><td></td></tr>
        <tr><td></td><td></td><td></td><td></td><td></td><td></td><td></td><td></td><td></td></tr>
      </tbody>
    </table>
  </section>

  <aside class="notes"><h2>NOTES</h2></aside>

  <section class="panel small tasks-6">
    <div class="panel-title">6 Monthly Tasks</div>
    <table>
      <thead><tr><th>Tasks</th><th>Due Date</th></tr></thead>
      <tbody>
        <tr><td>Operations Manual</td><td></td></tr>
        <tr><td>Staff Meeting</td><td></td></tr>
        <tr><td>SMS Meeting</td><td></td></tr>
        <tr><td>Fire Extinguisher Inspection</td><td></td></tr>
        <tr><td>Flight Instrument Inspection</td><td></td></tr>
        <tr><td></td><td></td></tr>
        <tr><td></td><td></td></tr>
        <tr><td></td><td></td></tr>
      </tbody>
    </table>
  </section>

  <section class="panel small tasks-12">
    <div class="panel-title">12 Monthly Tasks</div>
    <table>
      <thead><tr><th>Tasks</th><th>Due Date</th></tr></thead>
      <tbody>
        <tr><td>COA Internal Audit</td><td></td></tr>
        <tr><td>SMS Audit</td><td></td></tr>
        <tr><td>Fatigue Training</td><td></td></tr>
        <tr><td>CAO 20.11</td><td></td></tr>
        <tr><td></td><td></td></tr>
        <tr><td></td><td></td></tr>
        <tr><td></td><td></td></tr>
        <tr><td></td><td></td></tr>
      </tbody>
    </table>
  </section>

  <section class="panel small schedule">
    <div class="panel-title">Balloon Annual / Periodic Schedule</div>
    <table>
      <thead><tr><th>Balloon</th><th>Type</th><th>Annual Date</th><th>Periodic Time</th></tr></thead>
      <tbody>
        <tr><td>VH-QLB</td><td>Strato D90</td><td></td><td></td></tr>
        <tr><td>VH-QLX</td><td>Strato E180</td><td></td><td></td></tr>
        <tr><td>VH-QLZ</td><td>Strato E240</td><td></td><td></td></tr>
        <tr><td>VH-QLV</td><td>Strato B400</td><td></td><td></td></tr>
        <tr><td>VH-QLT</td><td>Strato G450</td><td></td><td></td></tr>
        <tr><td></td><td></td><td></td><td></td></tr>
        <tr><td></td><td></td><td></td><td></td></tr>
        <tr><td></td><td></td><td></td><td></td></tr>
      </tbody>
    </table>
  </section>

  <footer class="footer">
    <span>Highland Aerostats Pty Ltd T/A Skyward Ballooning</span>
    <span>CASA AOC: S700214</span>
    <span>Certificate of Approval: 5186</span>
  </footer>
</div>
</body>
</html>
```